The Pane Masters- we supply and install new windows for customers homes

We require a 12 page brochure (8 pages with a cover) This is to be finished 8.5 x 11 with the layout to be 17.25" x 11.25" (full bleed). These pages will be folded and saddlestitched to the finished size. We require our designer to be familiar with print layouts. I have attached a flow sheet in word that describes the content of each page. Additionally I have picture files co-ordinated to each page. Please provide a sample layout of any page for review and selection. Our colour themes as indicated in our logo are CMYK 0 80 100 0 and CMYK 65 58 58 38. We have no concept as to design but it must look professional. Upon successful selection all of the files would be made available

```html
<!DOCTYPE html>
<html lang="en">
<head>
<meta charset="utf-8">
<title>The Pane Masters – Brochure Cover</title>
<link rel="stylesheet" href="https://fonts.googleapis.com/css2?family=Open+Sans:wght@600;700&display=swap">
<style>
  :root {
    --backdrop: #a9a9ad;
    --paper: #f6f6f7;
    --facet-light: #ececee;
    --facet-mid: #e2e2e5;
    --brand-orange: #e0502a;
    --brand-orange-deep: #d24a1c;
    --brand-grey: #4b4a4b;
    --photo-sky: #3d66b4;
    --photo-dusk: #6d8ec8;
    --photo-house: #c9b98d;
    --photo-lawn: #3d5a32;
  }
  * { margin: 0; padding: 0; box-sizing: border-box; }
  html, body {
    width: 1200px;
    height: 900px;
    overflow: hidden;
    background: var(--backdrop);
  }
  .stage {
    position: relative;
    width: 1200px;
    height: 900px;
  }
  .brochure-cover {
    position: absolute;
    left: 280px;
    top: 36px;
    width: 640px;
    height: 828px;
    background: var(--paper);
    box-shadow: 0 6px 18px rgba(0, 0, 0, 0.18);
  }
  .brochure-cover svg {
    display: block;
    width: 100%;
    height: 100%;
  }
  .facet-light { fill: var(--facet-light); }
  .facet-mid { fill: var(--facet-mid); }
  .accent-upper { fill: var(--brand-orange); }
  .accent-lower { fill: var(--brand-orange-deep); }
  .brand-name {
    font-family: "Open Sans", sans-serif;
    font-weight: 700;
    font-size: 17px;
    letter-spacing: 2.5px;
    fill: var(--brand-orange);
  }
  .brand-mark { fill: var(--brand-orange); }
  .cover-title {
    font-family: "Open Sans", sans-serif;
    font-weight: 700;
    font-size: 25px;
    letter-spacing: 5px;
    fill: var(--brand-grey);
  }
</style>
</head>
<body>
<main class="stage">
  <article class="brochure-cover">
    <svg viewBox="0 0 612 792" xmlns="http://www.w3.org/2000/svg">
      <defs>
        <linearGradient id="photoTones" x1="0" y1="0" x2="0" y2="1">
          <stop offset="0" stop-color="var(--photo-sky)"/>
          <stop offset="0.35" stop-color="var(--photo-dusk)"/>
          <stop offset="0.6" stop-color="var(--photo-house)"/>
          <stop offset="1" stop-color="var(--photo-lawn)"/>
        </linearGradient>
      </defs>

      <g class="background-facets">
        <polygon class="facet-light" points="300,0 612,0 612,250 380,220"/>
        <polygon class="facet-mid" points="0,60 130,0 300,0 200,300"/>
        <polygon class="facet-light" points="260,560 612,520 612,792 430,792"/>
        <polygon class="facet-mid" points="330,640 612,700 612,792"/>
      </g>

      <g class="orange-accents">
        <polygon class="accent-upper" points="0,40 175,345 0,560"/>
        <polygon class="accent-lower" points="175,345 262,560 150,792 88,792 70,600"/>
      </g>

      <g class="brand-lockup">
        <rect class="brand-mark" x="345" y="174" width="16" height="16"/>
        <text class="brand-name" x="370" y="189">PANE MASTERS</text>
      </g>

      <polygon class="cover-photo" role="img"
        aria-label="Photograph of a two-storey house with a wrap-around porch, lit at dusk, with a curving stone path across the lawn"
        fill="url(#photoTones)"
        points="175,345 612,262 612,520 262,560"/>

      <text class="cover-title" text-anchor="end">
        <tspan x="585" y="602">THE PANE</tspan>
        <tspan x="585" y="634">MASTERS</tspan>
      </text>
    </svg>
  </article>
</main>
</body>
</html>
```